korrivan global sell sheet brochure

I need two pages of text and photos that would represent a sell sheet featuring three products.
1) canopy tents
2) canopy benches ( six seat)
3) Canopy seat ( two seat)

The dolly (trolley) photo goes with the six seat bench.
The two seat collage can be separated.

```html
<!DOCTYPE html>
<html lang="en">
<head>
<meta charset="utf-8">
<title>korrivan global sell sheet</title>
<link rel="stylesheet" href="https://fonts.googleapis.com/css2?family=Jost:wght@400;500;700;800&display=swap">
<style>
:root{
  --navy:#2a4a9b;
  --navy-deep:#21408e;
  --ink:#1d1d1f;
  --sky-top:#f4f6fb;
  --sky-bottom:#8fa9d6;
  --box:#d5dff0;
  --box-line:#b9c6e0;
  --gallery:#d7d9de;
  --red:#d8262c;
  --white:#ffffff;
}
*{margin:0;padding:0;box-sizing:border-box}
html,body{width:927px;height:1200px;overflow:hidden}
body{font-family:"Jost",Arial,sans-serif;color:var(--ink);
  background:linear-gradient(180deg,var(--white) 0%,var(--sky-top) 20%,#c9d6ec 60%,var(--sky-bottom) 100%);
  position:relative}
.sheet{position:absolute;inset:0}
.product-circle{position:absolute;width:235px;height:200px;border-radius:50%;background:var(--white);
  display:flex;align-items:center;justify-content:center}
.product-circle.left{left:48px;top:22px}
.product-circle.right{left:652px;top:22px}
.photo{display:block}
.two-seat{position:absolute;left:300px;top:60px;width:330px}
.two-seat h2{font-size:27px;font-weight:700;color:var(--navy);margin-bottom:6px}
ul.points{list-style:none}
ul.points li{position:relative;padding-left:18px;font-size:17px;line-height:21px;margin-bottom:5px}
ul.points li::before{content:"";position:absolute;left:0;top:6px;width:9px;height:9px;background:var(--ink)}
.price{font-weight:500;font-size:19px}
.history-title{position:absolute;left:0;width:927px;top:218px;text-align:center;font-size:36px;font-weight:700;color:var(--navy)}
.history-band{position:absolute;left:53px;top:272px;width:826px;height:104px;background:var(--navy);border-radius:6px;
  color:var(--white);font-size:17px;line-height:24px;padding:4px 16px}
.promo-title{position:absolute;left:72px;top:388px;font-size:37px;font-weight:700;color:var(--navy)}
.promo-list{position:absolute;left:74px;top:440px;width:640px}
.promo-list li{font-size:16.5px;line-height:21px;margin-bottom:6px}
.promo-list .strong{font-weight:500;font-size:17.5px}
.bench-bag{position:absolute;left:757px;top:384px}
.fund-title{position:absolute;left:72px;top:648px;font-size:36px;line-height:40px;font-weight:800;color:var(--navy)}
.fund-option{position:absolute;left:73px;width:776px;background:var(--box);border:1px solid var(--box-line);
  font-size:17px;line-height:22px;padding:8px 16px}
.fund-option .dot{display:inline-block;width:9px;height:9px;background:var(--ink);margin-right:8px;vertical-align:2px}
.opt-1{top:742px;height:38px}
.opt-2{top:786px;height:40px}
.opt-3{top:828px;height:76px;padding-top:6px}
.gallery{position:absolute;left:73px;top:917px;width:776px;height:154px;background:var(--gallery);border:1px solid #c4c7cd;border-radius:3px;
  display:flex;align-items:center;justify-content:space-around;padding:0 10px}
.contact-bar{position:absolute;left:0;top:1093px;width:927px;height:66px;background:var(--white)}
.contact-tab{position:absolute;left:0;top:0;width:214px;height:66px;background:var(--navy-deep);
  clip-path:polygon(0 0,100% 0,92% 100%,0 100%);color:var(--white);font-size:26px;font-weight:700;
  white-space:nowrap;display:flex;align-items:center;padding-left:70px}
.contact-text{position:absolute;left:214px;right:60px;top:8px;text-align:center;color:var(--navy-deep);font-size:17.5px;font-weight:500;line-height:24px}
</style>
</head>
<body>
<main class="sheet">
  <div class="product-circle left">
    <svg class="photo" width="170" height="140" role="img" aria-label="Red two seat canopy chair with cooler, front view"><rect width="170" height="140" rx="14" fill="var(--red)"/></svg>
  </div>
  <section class="two-seat">
    <h2>Two seat with Cooler</h2>
    <ul class="points">
      <li>Great for parents watching with all the benefits of the six seater.</li>
      <li>Retail <span class="price">$120</span>, clubs can purchase for <span class="price">$80</span> and resell to fundraise.</li>
    </ul>
  </section>
  <div class="product-circle right">
    <svg class="photo" width="170" height="140" role="img" aria-label="Red two seat canopy chair with canopy folded back"><rect width="170" height="140" rx="14" fill="var(--red)"/></svg>
  </div>

  <h2 class="history-title">History</h2>
  <p class="history-band">The canopy bench is a patent CDN product that has been on Founders' Pitch first season and has won countless awards for its innovation.&nbsp; It has been around for 9 years and has been branded with many great names like Northway, Fresh Roll, Maple Brew, Harbour Lager, Kaido Motors, PGL, Pro Ice League, Strikeline, Velocita and many more.</p>

  <h2 class="promo-title">The Promotion</h2>
  <ul class="points promo-list">
    <li>We offer free screening on Club orders of Club logo and Club sponsors over 25 units.</li>
    <li>Retail for our benches is $250, plus shipping.</li>
    <li class="strong">We are offering you a special price of $150, plus shipping and applicable taxes.&nbsp; Shipping costs by container are&nbsp; $10 per unit.</li>
    <li>Tents are $900.&nbsp; Early since pre-orders are $450, plus shipping and taxes.</li>
    <li>Side flaps are optional for $25 per side.</li>
  </ul>
  <svg class="bench-bag" width="122" height="222" role="img" aria-label="Six seat canopy bench packed on its dolly in a blue sponsor-printed cover"><rect x="0" y="0" width="122" height="205" rx="10" fill="#2f5aa6"/><rect x="0" y="198" width="122" height="24" fill="#1b1b1f"/></svg>

  <h2 class="fund-title">There are a couple of different ways<br>to fund your bench.</h2>
  <p class="fund-option opt-1"><span class="dot"></span>Outright purchase</p>
  <p class="fund-option opt-2"><span class="dot"></span>Sponsor buys the bench for you. ( Usually, a parent&nbsp; owning a business)</p>
  <p class="fund-option opt-3"><span class="dot"></span>Use the parents two seat bench to fundraise.&nbsp; We will give you $40 per two seat with cooler, so That is only four sales of two seat with cooler to fund your bench.&nbsp; Retails for $120.</p>

  <div class="gallery">
    <svg width="108" height="120" role="img" aria-label="Red two seat canopy chair"><rect width="108" height="120" rx="10" fill="var(--red)"/></svg>
    <svg width="108" height="120" role="img" aria-label="Blue six seat canopy bench, rear view"><rect width="108" height="120" rx="10" fill="#2c4f9c"/></svg>
    <svg width="150" height="120" role="img" aria-label="Blue six seat canopy bench with club sponsor print"><rect width="150" height="120" rx="10" fill="#2f5aa6"/></svg>
    <svg width="120" height="120" role="img" aria-label="Black canopy tent with club name on the valance"><rect width="120" height="120" rx="6" fill="#34363c"/></svg>
    <svg width="108" height="120" role="img" aria-label="Red two seat canopy chair with cooler"><rect width="108" height="120" rx="10" fill="var(--red)"/></svg>
  </div>

  <footer class="contact-bar">
    <div class="contact-tab">Contact us</div>
    <p class="contact-text">Contact us for a quote or how we can help you get your team bench or tent.<br>Toll Free: 1.877.555.0142</p>
  </footer>
</main>
</body>
</html>
```